I'm an electrician and the name of my company is called Brisk 'N' Bright Electrical. I require a professional business card that speaks to my clients, I also need it to be innovative and modern. We do maintenance & service work for domestic and commercial premises.

Industry/Entity Type

Electrical

Contact Information for Business Card

Must have the name of my company Brisk 'N' Bright Electrical, my name Darren Kolovos and my contact details 0427 381 592 and company email address Brisknbrightelectrical@mailvane.com and/or website Brisknbrightelectrical.com.au

Logo Text

Brisk 'N' Bright Electrical (If possible)

Colors
33a6d7
0592cd
3176b5

```html
<!DOCTYPE html>
<html lang="en">
<head>
<meta charset="utf-8">
<title>Brisk 'N' Bright Electrical — Business Card</title>
<link href="https://fonts.googleapis.com/css2?family=Roboto:wght@400;700;900&display=swap" rel="stylesheet">
<style>
  :root {
    --backdrop: #4d4d4d;
    --card: #1e1d1f;
    --accent: #0592cd;
    --accent-light: #33a6d7;
    --accent-edge: #3176b5;
    --text-light: #f2f2f2;
    --divider: #8a8a8a;
    --emboss: #2b2a2c;
  }
  * { margin: 0; padding: 0; box-sizing: border-box; }
  html, body {
    width: 1200px; height: 800px; overflow: hidden;
    background: var(--backdrop);
    font-family: "Roboto", Arial, sans-serif;
  }
  .stage {
    width: 1200px; height: 800px;
    display: flex; flex-direction: column;
    align-items: center; justify-content: center; gap: 40px;
  }
  .card {
    width: 560px; height: 320px;
    background: var(--card);
    border-bottom: 3px solid var(--accent-edge);
    box-shadow: 0 14px 30px rgba(0,0,0,.35);
    position: relative;
  }
  .card--front { display: flex; align-items: center; }
  .brand {
    width: 280px; display: flex; align-items: center; justify-content: center; gap: 12px;
  }
  .brand__dot {
    width: 22px; height: 22px; border-radius: 50%; background: var(--accent); flex: none;
  }
  .brand__name {
    color: var(--text-light); font-weight: 900; font-size: 21px; line-height: 1.15;
    text-transform: uppercase;
  }
  .divider {
    width: 1px; height: 90px; background: var(--divider); opacity: .7;
  }
  .contact { padding-left: 24px; }
  .contact__name {
    color: var(--accent-light); font-weight: 700; font-size: 22px;
    text-transform: uppercase; letter-spacing: .3px; margin-bottom: 12px;
  }
  .contact__list { list-style: none; }
  .contact__item {
    display: flex; align-items: center; gap: 8px;
    color: var(--text-light); font-size: 12.5px; line-height: 1.7;
  }
  .contact__icon { width: 11px; height: 11px; flex: none; }
  .card--back { display: flex; align-items: center; justify-content: center; gap: 16px; }
  .back-mark__dot {
    width: 44px; height: 44px; border-radius: 50%; background: var(--emboss); flex: none;
  }
  .back-mark__name {
    color: var(--emboss); font-weight: 900; font-size: 36px; line-height: 1.1;
    text-transform: uppercase;
  }
</style>
</head>
<body>
<main class="stage">
  <section class="card card--front">
    <div class="brand">
      <span class="brand__dot"></span>
      <span class="brand__name">Brisk 'N' Bright<br>Electrical</span>
    </div>
    <span class="divider"></span>
    <div class="contact">
      <h1 class="contact__name">Darren Kolovos</h1>
      <ul class="contact__list">
        <li class="contact__item">
          <svg class="contact__icon" viewBox="0 0 12 12"><path fill="var(--accent)" d="M2.5 1h2l1 3-1.3 1a6 6 0 0 0 2.8 2.8L8 6.5l3 1v2A1.5 1.5 0 0 1 9.5 11 8.5 8.5 0 0 1 1 2.5 1.5 1.5 0 0 1 2.5 1z"/></svg>
          0427 381 592
        </li>
        <li class="contact__item">
          <svg class="contact__icon" viewBox="0 0 12 12"><rect x="0.5" y="2" width="11" height="8" fill="var(--accent)"/><path d="M1 2.5l5 4 5-4" fill="none" stroke="var(--card)" stroke-width="1"/></svg>
          Brisknbrightelectrical@mailvane.com
        </li>
        <li class="contact__item">
          <svg class="contact__icon" viewBox="0 0 12 12"><circle cx="6" cy="6" r="5.5" fill="var(--accent)"/><path d="M.5 6h11M6 .5c-2.5 3-2.5 8 0 11M6 .5c2.5 3 2.5 8 0 11" fill="none" stroke="var(--card)" stroke-width=".8"/></svg>
          www.Brisknbrightelectrical.com.au
        </li>
      </ul>
    </div>
  </section>

  <section class="card card--back">
    <span class="back-mark__dot"></span>
    <span class="back-mark__name">Brisk 'N' Bright<br>Electrical</span>
  </section>
</main>
</body>
</html>
```